Flyer for annual KESTREL SUMMIT 2020

I would like a church event flyer designed. The event is called "KESTREL SUMMIT 2020". I am looking for a professional, yet catchy design that uses our brand colors and logo creatively while communicating key information of the event effectively.

1. The logo is attached in two color formats. The designer has the choice to use them as he/she want.

2. The location of the event is: Harlow Community Center, 239 Fennimore Street, Portland, ME 04117

3. Time and date of event. The designer can organize and format the date and time as he/she pleases.
Thursday December 31st @ 6:30PM
Friday January 1st @ 6:30PM
Saturday 2nd @ 6:30PM
Sunday 3rd @ 4:30PM

4. The topic of the event is "In Fire and On Fire". The designer is free to use this phrase as he/she pleases to create a good composition.

5. Speaker: Prophet Marcus Olunde (2 pictures of the speaker to choose from are attached)

6. Contact information: contact@brightmeadowfold.org - Telephone number: 207 583 2914

7. I would also like the following three words on the flyer. These words describe the focus of the event: FIRE, REVIVAL, PROPHETIC

Target Market(s)

Young adults

Font styles to use
Sans Serif

Requirements
Must have
• Logo, speaker's picture
Should not have
• cross image, church image

```html
<!DOCTYPE html>
<html lang="en">
<head>
<meta charset="utf-8">
<title>Kestrel Summit 2020 – In Fire &amp; On Fire</title>
<link href="https://fonts.googleapis.com/css2?family=Montserrat:wght@300;400;700;900&display=swap" rel="stylesheet">
<style>
  :root{
    --violet:#8a33f5;
    --violet-deep:#4a12b4;
    --violet-night:#3a0f9e;
    --violet-hatch:#7a2ae6;
    --lavender:#a77cf7;
    --flame-pink:#e0329a;
    --flame-orange:#ff6a3a;
    --suit-red:#e0441f;
    --ember:#ff8a1c;
    --white:#ffffff;
  }
  *{margin:0;padding:0;box-sizing:border-box}
  html,body{width:848px;height:1200px;overflow:hidden;background:var(--violet)}
  .flyer{position:relative;width:848px;height:1200px;overflow:hidden;background:var(--violet);
    font-family:'Montserrat',sans-serif;color:var(--white)}
  .backdrop,.hero,.ornaments{position:absolute;left:0;top:0}
  .abs{position:absolute}

  .event-title{left:40px;top:74px;font-size:25px;letter-spacing:4px;line-height:32px}
  .event-title .light{font-weight:300}
  .event-title .bold{font-weight:900}
  .title-rule{left:42px;top:150px;width:257px;height:4px;background:var(--white)}
  .theme{left:40px;top:176px;font-weight:900;font-size:52px;letter-spacing:9px;line-height:62px}

  .brand{right:19px;top:82px;display:flex;align-items:center;gap:10px}
  .brand-dot{width:14px;height:14px;border-radius:50%;background:var(--ember)}
  .brand-name{font-weight:400;font-size:40px;letter-spacing:2px;line-height:44px}

  .speaker{right:19px;top:312px;text-align:right;width:200px}
  .speaker-label{font-weight:400;font-size:17px;letter-spacing:5px}
  .speaker-rule{height:4px;background:var(--white);margin:10px 0 10px}
  .speaker-role{font-weight:900;font-size:16px;letter-spacing:4px}
  .speaker-name{font-weight:900;font-size:34px;letter-spacing:5px;line-height:45px;margin-top:4px}

  .focus{left:38px;top:410px;writing-mode:vertical-rl;font-weight:400;font-size:20px;letter-spacing:5px}

  .schedule{left:560px;top:908px;width:152px;text-align:right}
  .slot{height:63.5px}
  .slot-day{font-weight:400;font-size:17px;line-height:22px}
  .slot-time{font-weight:300;font-size:31px;letter-spacing:5px;line-height:32px}
  .slot-time small{font-size:16px;letter-spacing:0;font-weight:400}
  .schedule-rule{left:731px;top:897px;width:4px;height:303px;background:var(--white)}
  .dates{left:740px;top:894px;width:86px;text-align:right}
  .date-month{font-weight:300;font-size:29px;letter-spacing:5px;line-height:31px}
  .date-day{font-weight:900;font-size:27px;line-height:31px}

  .venue{left:103px;top:1049px;font-weight:700;font-size:16px;letter-spacing:4.3px;line-height:18.5px}
  .venue-rule{left:103px;top:1120px;width:51px;height:4px;background:var(--white)}
  .contact{left:103px;top:1131px;font-weight:700;font-size:19px;line-height:21px}
</style>
</head>
<body>
<main class="flyer">

  <svg class="backdrop" width="848" height="1200" viewBox="0 0 848 1200" aria-hidden="true">
    <defs>
      <pattern id="hatch" width="5" height="5" patternUnits="userSpaceOnUse" patternTransform="rotate(-35)">
        <rect width="5" height="5" fill="var(--violet-hatch)"/>
        <line x1="0" y1="0" x2="0" y2="5" stroke="#9b5cf7" stroke-width="1" opacity=".5"/>
      </pattern>
    </defs>
    <rect width="848" height="1200" fill="var(--violet)"/>
    <polygon points="640,230 848,120 848,1200 250,1200" fill="url(#hatch)"/>
    <polygon points="362,0 848,0 848,287" fill="var(--violet-deep)"/>
    <polygon points="0,910 534,1200 0,1200" fill="var(--violet-night)"/>
    <line x1="735" y1="0" x2="260" y2="1200" stroke="#ffffff" stroke-width="1" stroke-dasharray="2 3" opacity=".35"/>
    <line x1="0" y1="455" x2="848" y2="900" stroke="#ffffff" stroke-width="1" stroke-dasharray="2 3" opacity=".3"/>
  </svg>

  <svg class="hero" width="848" height="1200" viewBox="0 0 848 1200">
    <defs>
      <radialGradient id="flame" cx="50%" cy="50%" r="50%">
        <stop offset="70%" stop-color="var(--flame-pink)"/>
        <stop offset="88%" stop-color="var(--flame-orange)"/>
        <stop offset="100%" stop-color="#c22fd6"/>
      </radialGradient>
      <linearGradient id="portrait" x1="0" y1="0" x2="0" y2="1">
        <stop offset="0" stop-color="#3a2a2a"/>
        <stop offset=".25" stop-color="var(--suit-red)"/>
        <stop offset="1" stop-color="#c7361a"/>
      </linearGradient>
    </defs>
    <circle cx="383" cy="626" r="311" fill="none" stroke="#ffffff" stroke-width="2.5" stroke-dasharray="0.1 6" stroke-linecap="round"/>
    <circle cx="375" cy="629" r="280" fill="url(#flame)" role="img" aria-label="Flame texture ring"/>
    <circle cx="375" cy="629" r="198" fill="var(--lavender)"/>
    <circle cx="373" cy="545" r="170" fill="none" stroke="#ffffff" stroke-width="1.2"/>
    <path d="M330 310 Q373 300 416 310 L430 440 Q500 460 510 520 L512 814 L192 814 L196 520 Q210 460 320 440 Z"
          fill="url(#portrait)" role="img" aria-label="Portrait of Prophet Marcus Olunde in a red suit"/>
  </svg>

  <svg class="ornaments" width="848" height="1200" viewBox="0 0 848 1200" aria-hidden="true" fill="none" stroke="#ffffff" stroke-width="2.5">
    <g>
      <rect x="507" y="178" width="10" height="10"/><rect x="507" y="207" width="10" height="10"/>
      <rect x="507" y="236" width="10" height="10"/><rect x="507" y="265" width="10" height="10"/>
      <rect x="507" y="294" width="10" height="10"/><rect x="507" y="323" width="10" height="10"/>
      <rect x="507" y="352" width="10" height="10"/>
    </g>
    <g>
      <rect x="827" y="621" width="10" height="10"/><rect x="827" y="650" width="10" height="10"/>
      <rect x="827" y="679" width="10" height="10"/><rect x="827" y="708" width="10" height="10"/>
      <rect x="827" y="737" width="10" height="10"/><rect x="827" y="766" width="10" height="10"/>
      <rect x="827" y="795" width="10" height="10"/>
    </g>
    <rect x="748" y="587" width="13" height="13"/>
    <rect x="102" y="508" width="8" height="8"/>
    <circle cx="98" cy="327" r="9"/>
    <circle cx="96" cy="536" r="7"/>
    <circle cx="564" cy="882" r="12"/>
    <circle cx="621" cy="798" r="7" fill="#ffffff" stroke="none"/>
    <rect x="7" y="999" width="11" height="11"/><rect x="37" y="999" width="11" height="11"/><rect x="67" y="999" width="11" height="11"/>
    <g fill="#ffffff" stroke="none">
      <rect x="21" y="1137" width="13" height="13"/><rect x="45" y="1137" width="13" height="13"/><rect x="45" y="1158" width="13" height="13"/>
    </g>
  </svg>

  <header>
    <h2 class="abs event-title"><span class="light">2020 | </span><span class="bold">KESTREL<br>SUMMIT</span></h2>
    <div class="abs title-rule"></div>
    <h1 class="abs theme">IN FIRE &amp;<br>ON FIRE</h1>
  </header>

  <div class="abs brand">
    <span class="brand-dot"></span>
    <span class="brand-name">ORVELLE</span>
  </div>

  <section class="abs speaker">
    <p class="speaker-label">SPEAKER</p>
    <div class="speaker-rule"></div>
    <p class="speaker-role">PROPHET</p>
    <p class="speaker-name">MARCUS<br>OLUNDE</p>
  </section>

  <p class="abs focus">FIRE | REVIVAL | PROPHETIC</p>

  <section class="abs schedule">
    <div class="slot"><p class="slot-day">Thursday</p><p class="slot-time">6:30<small>PM</small></p></div>
    <div class="slot"><p class="slot-day">Friday</p><p class="slot-time">6:30<small>PM</small></p></div>
    <div class="slot"><p class="slot-day">Saturday</p><p class="slot-time">6:30<small>PM</small></p></div>
    <div class="slot"><p class="slot-day">Sunday</p><p class="slot-time">4:30<small>PM</small></p></div>
  </section>
  <div class="abs schedule-rule"></div>
  <section class="abs dates">
    <p class="date-month">Dec</p><p class="date-day">31</p>
    <p class="date-month">Jan</p><p class="date-day">1</p>
    <p class="date-month">Jan</p><p class="date-day">2</p>
    <p class="date-month">Jan</p><p class="date-day">3</p>
  </section>

  <address class="abs venue" style="font-style:normal">HARLOW COMMUNITY CENTER<br>239 FENNIMORE STREET<br>PORTLAND, ME 04117</address>
  <div class="abs venue-rule"></div>
  <p class="abs contact">contact@brightmeadowfold.org<br>Telephone Number - 207 583 2914</p>

</main>
</body>
</html>
```